Business Card design for construction company

I would like a business card design for a construction company - Harlow Constructions. I have attached the ai logo file for use. I would like the card to be very smart and clean and incorporate only white and the two colours in the logo. I would like the card to have two sides. One side can just have the logo, the other with the relevant information.

Target Market(s)

Building and Construction Clients

Industry/Entity Type

Business

Contact Information for Business Card

Name: Tom Pardoe
Company: Harlow Constructions Pty Limited
Address: 14 Mallee Crescent Carrow Vale 2093
Phone: 0427 531 068
Email: tomp@harlowbuild-example.com.au

Font styles to use
Serif
Sans Serif

Requirements
Must have
• Details noted above
• Logo as provided
• Colours as in logo
• Square edges
• A font that compliments the logo
Should not have
• Any colour other than white and those in logo
• Rounded edges

```html
<!DOCTYPE html>
<html lang="en">
<head>
<meta charset="utf-8">
<title>Harlow Constructions – Business Card</title>
<link rel="stylesheet" href="https://fonts.googleapis.com/css2?family=Oswald:wght@500&family=Roboto:wght@400&display=swap">
<style>
  :root {
    --backdrop: #1b1b1b;
    --card-grey: #555555;
    --mark-grey: #3f3f3f;
    --ink: #4a4a4a;
    --accent: #1ea5e0;
    --paper: #ffffff;
  }
  * { margin: 0; padding: 0; box-sizing: border-box; }
  html, body { width: 1200px; height: 1200px; overflow: hidden; }
  body {
    background: var(--backdrop);
    font-family: "Roboto", Arial, sans-serif;
    display: flex;
    flex-direction: column;
    align-items: center;
    justify-content: center;
    gap: 60px;
  }
  .card {
    width: 840px;
    height: 480px;
    position: relative;
  }
  .card-back {
    background: var(--card-grey);
    display: flex;
    align-items: center;
    justify-content: center;
  }
  .card-back .company-name {
    color: var(--mark-grey);
    font-size: 40px;
    letter-spacing: 4px;
    text-transform: uppercase;
  }
  .card-front { background: var(--paper); }
  .identity {
    position: absolute;
    right: 400px;
    top: 178px;
    text-align: right;
  }
  .person-name {
    font-family: "Oswald", "Arial Narrow", sans-serif;
    font-weight: 500;
    font-size: 44px;
    line-height: 1;
    color: var(--ink);
    letter-spacing: -0.5px;
  }
  .person-role {
    color: var(--accent);
    font-size: 21px;
    margin-top: 4px;
  }
  .divider {
    position: absolute;
    left: 462px;
    top: 168px;
    width: 2px;
    height: 100px;
    background: var(--accent);
  }
  .contact-list {
    position: absolute;
    left: 488px;
    top: 170px;
    list-style: none;
    color: var(--ink);
    font-size: 18px;
  }
  .contact-list li {
    display: flex;
    align-items: center;
    gap: 10px;
    height: 32px;
  }
  .contact-list svg { width: 16px; height: 16px; fill: var(--accent); flex: none; }
  .footer-line {
    position: absolute;
    left: 200px;
    bottom: 52px;
    display: flex;
    align-items: center;
    gap: 10px;
    color: var(--ink);
    font-size: 19px;
  }
  .footer-line .company-name {
    font-size: 13px;
    letter-spacing: 2px;
    text-transform: uppercase;
    color: var(--ink);
  }
</style>
</head>
<body>
  <section class="card card-back">
    <span class="company-name">Harlow Constructions</span>
  </section>

  <section class="card card-front">
    <div class="identity">
      <div class="person-name">TOM PARDOE</div>
      <div class="person-role">CEO/Founder</div>
    </div>
    <div class="divider"></div>
    <ul class="contact-list">
      <li>
        <svg viewBox="0 0 16 16" aria-hidden="true"><path d="M3.5 1.5l2.5 2.8-1.4 1.8c.9 2 2.4 3.5 4.4 4.4l1.8-1.4 2.8 2.5-1.6 2.4C6.8 13.8 2.2 9.2 1.1 3.1z"/></svg>
        0427 531 068
      </li>
      <li>
        <svg viewBox="0 0 16 16" aria-hidden="true"><path d="M1 3h14v10H1z M1.5 3.5L8 9l6.5-5.5" fill="none" stroke="#1ea5e0" stroke-width="1.6"/></svg>
        tomp@harlowbuild-example.com.au
      </li>
      <li>
        <svg viewBox="0 0 16 16" aria-hidden="true" fill="none" stroke="#1ea5e0" stroke-width="1.3"><circle cx="8" cy="8" r="6.5"/><ellipse cx="8" cy="8" rx="3" ry="6.5"/><path d="M1.5 8h13M2.5 4.5h11M2.5 11.5h11"/></svg>
        www.harlowbuild-example.com.au
      </li>
    </ul>
    <div class="footer-line">
      <span class="company-name">Harlow Constructions</span>
      <span>: 14 Mallee Crescent Carrow Vale 2093</span>
    </div>
  </section>
</body>
</html>
```